Corwin Tably Interiors
business card and stationary
Corwin Tably Interiors -
Creative Brief
Simple
corwin tably
interior designer
studio: 27 brookfen lane pacifica, california 94044
corwin@corwintablyinteriors.example
http://corwintablyinteriors.example
the graphic part of my logo is something i will use a lot in my branding. i like the idea of repitition or a very large version of it in a single color or grayscale that bleeds off the card.
i like the grayscale logo (white burst) on the gray background a lot. i want one side of the card to be white background, probably the front.

```html
<!DOCTYPE html>
<html lang="en">
<head>
<meta charset="utf-8">
<title>Corwin Tably Interiors – Business Card</title>
<link rel="stylesheet" href="https://fonts.googleapis.com/css2?family=Questrial&display=swap">
<style>
  :root {
    --stage: #2a2a2b;
    --card-gray: #8b8c8e;
    --card-white: #ffffff;
    --ink-white: #ffffff;
    --ink-gray: #7c7d80;
    --brand-green: #a9d68f;
    --brand-green-soft: #dcefd0;
    --mark-light: #d9dadb;
  }
  * { box-sizing: border-box; margin: 0; padding: 0; }
  html, body { width: 1200px; height: 751px; overflow: hidden; }
  body {
    background: var(--stage);
    font-family: "Questrial", "Century Gothic", sans-serif;
    position: relative;
  }
  .card {
    position: absolute;
    top: 211px;
    width: 552px;
    height: 382px;
    overflow: hidden;
  }
  .card--back { left: 24px; background: var(--card-gray); }
  .card--front { left: 624px; background: var(--card-white); }

  .brand-dot {
    position: absolute;
    left: 14px; top: 26px;
    width: 112px; height: 112px;
  }
  .wordmark {
    position: absolute;
    right: 26px; top: 266px;
    text-align: right;
    color: var(--ink-white);
  }
  .wordmark__name {
    font-size: 50px;
    letter-spacing: -1px;
    line-height: 1;
  }
  .wordmark__tag {
    font-size: 13px;
    letter-spacing: 14.4px;
    margin-right: -14px;
    margin-top: 4px;
    text-transform: uppercase;
  }

  .brand-field {
    position: absolute;
    left: -90px; top: -40px;
    width: 470px; height: 470px;
  }
  .identity {
    position: absolute;
    right: 22px; top: 20px;
    text-align: right;
  }
  .identity__name {
    color: var(--brand-green);
    font-size: 28px;
    letter-spacing: -0.5px;
    line-height: 1;
  }
  .identity__role {
    color: var(--ink-gray);
    font-size: 15px;
    margin-top: 2px;
  }
  .contact {
    position: absolute;
    right: 22px; top: 283px;
    text-align: right;
    color: var(--ink-gray);
    font-size: 13.5px;
    line-height: 17px;
    font-style: normal;
  }
  .contact__gap { margin-top: 9px; }
</style>
</head>
<body>
  <section class="card card--back" aria-label="Card back">
    <svg class="brand-dot" viewBox="0 0 112 112" aria-hidden="true">
      <circle cx="56" cy="56" r="54" fill="var(--mark-light)"/>
    </svg>
    <div class="wordmark">
      <div class="wordmark__name">corwintably</div>
      <div class="wordmark__tag">Interiors</div>
    </div>
  </section>

  <section class="card card--front" aria-label="Card front">
    <svg class="brand-field" viewBox="0 0 470 470" role="img" aria-label="Large pale green brand graphic bleeding off the card edge">
      <defs>
        <radialGradient id="fieldTone" cx="50%" cy="50%" r="50%">
          <stop offset="0%" stop-color="var(--brand-green-soft)"/>
          <stop offset="100%" stop-color="var(--brand-green-soft)" stop-opacity="0.6"/>
        </radialGradient>
      </defs>
      <circle cx="235" cy="235" r="230" fill="url(#fieldTone)"/>
    </svg>
    <header class="identity">
      <div class="identity__name">corwintably</div>
      <div class="identity__role">interior designer</div>
    </header>
    <address class="contact">
      <div>studio: 27 brookfen lane</div>
      <div>larkhaven&nbsp; oregon 97381</div>
      <div>ph: 541.555.0142</div>
      <div class="contact__gap">corwin@corwintablyinteriors.example</div>
      <div>www.corwintablyinteriors.example</div>
    </address>
  </section>
</body>
</html>
```